A start up special flyer design!

Hi All - Have updated the attachment content - This is the info required for the designs.
I need a catchy flyer to send out to a few areas to advertise the start of my plumbing business!
The flyer will contain an offer for customers, which will need to have some key details on it. See attached. Feel free to fit these criteria into the flyer given your knowledge on design and messaging principles. Key thing to get across to customers is the discount and special offer, and that it is a start up offer.
I have a logo that needs to be on the flyer as well - let me know what format you require and I will send through to you.
The color scheme needs to be blue / grey / black / white.
Let me know if you have any questions.
I

```html
<!DOCTYPE html>
<html lang="en">
<head>
<meta charset="utf-8">
<title>Start Up Special Plumbing Flyer</title>
<link rel="stylesheet" href="https://fonts.googleapis.com/css2?family=Oswald:wght@500;600&family=Lato:wght@400;700;900&display=swap">
<style>
  :root {
    --stage: #e9ebee;
    --white: #ffffff;
    --blue: #1e7fd6;
    --blue-deep: #0f5fb0;
    --blue-bright: #35a2f0;
    --sky: #6ec3f5;
    --ink: #1c1c1e;
    --charcoal: #2b2d31;
    --grey: #8e9399;
    --grey-light: #e4e6e9;
    --grey-mid: #c9ccd0;
    --text-dark: #222426;
  }
  * { box-sizing: border-box; margin: 0; padding: 0; }
  html, body { width: 1200px; height: 912px; overflow: hidden; }
  body { background: var(--stage); font-family: "Lato", sans-serif; position: relative; }

  .flyer {
    position: absolute; left: 300px; top: 31px;
    width: 600px; height: 850px; background: var(--white);
    box-shadow: 0 8px 24px rgba(0,0,0,.18); overflow: hidden;
  }
  .flyer-shapes { position: absolute; inset: 0; }

  .brand-name {
    position: absolute; left: 34px; top: 40px;
    font-family: "Lato", sans-serif; font-weight: 400; font-size: 34px;
    letter-spacing: 2px; color: var(--blue-deep);
  }
  .services {
    position: absolute; right: 26px; top: 22px; text-align: right; line-height: 1.05;
  }
  .services .line-1 { font-size: 28px; color: var(--blue); font-weight: 400; }
  .services .line-2 { font-size: 30px; color: var(--charcoal); font-weight: 400; letter-spacing: 1px; }

  .headline {
    position: absolute; left: 300px; top: 160px; width: 285px; text-align: center;
    font-family: "Oswald", sans-serif; font-weight: 600; font-size: 36px; line-height: 1.12;
    color: var(--white); text-transform: uppercase;
  }
  .tagline {
    position: absolute; left: 300px; top: 250px; width: 285px; text-align: center;
    font-size: 25px; font-weight: 700; letter-spacing: 1.5px; color: var(--sky);
  }
  .gst-note {
    position: absolute; left: 305px; top: 305px; width: 280px; text-align: center;
    font-size: 20px; line-height: 1.2; color: var(--text-dark);
  }
  .gst-note strong { font-weight: 900; }

  .discount {
    position: absolute; left: 165px; top: 330px; width: 120px; text-align: center;
    color: var(--blue-deep);
  }
  .discount .amount { font-family: "Oswald", sans-serif; font-weight: 600; font-size: 25px; line-height: 1; }
  .discount .detail { font-size: 11px; font-weight: 900; color: var(--ink); margin-top: 2px; }

  .offer {
    position: absolute; left: 32px; top: 436px; width: 340px;
    color: var(--white); font-weight: 900; line-height: 1.1;
  }
  .offer .main { font-size: 29px; text-transform: uppercase; letter-spacing: .5px; }
  .offer .sub { font-size: 26px; }

  .call-to-action {
    position: absolute; left: 30px; top: 598px; width: 400px; line-height: 1.05;
  }
  .call-to-action .lead { font-size: 23px; font-weight: 900; color: var(--blue-bright); text-transform: uppercase; }
  .call-to-action .name { font-size: 31px; font-weight: 900; color: var(--blue-bright); text-transform: uppercase; }
  .call-to-action .alt { font-size: 15px; color: var(--white); margin-top: 4px; }

  .contact-list { position: absolute; left: 30px; top: 724px; list-style: none; }
  .contact-list li {
    display: flex; align-items: center; gap: 12px; height: 30px;
    font-size: 17px; color: var(--text-dark);
  }
  .contact-list svg { width: 16px; height: 16px; fill: var(--blue-deep); }

  .fine-print {
    position: absolute; right: 22px; top: 702px; text-align: right;
    font-size: 11px; line-height: 1.45; color: var(--charcoal);
  }
</style>
</head>
<body>
  <article class="flyer">
    <svg class="flyer-shapes" width="600" height="850" viewBox="0 0 600 850">
      <defs>
        <linearGradient id="blue-field" x1="0" y1="0" x2="1" y2="1">
          <stop offset="0" stop-color="#0f5fb0"/>
          <stop offset=".5" stop-color="#1e88e0"/>
          <stop offset="1" stop-color="#0f5fb0"/>
        </linearGradient>
        <linearGradient id="grey-box" x1="0" y1="0" x2="0" y2="1">
          <stop offset="0" stop-color="#ffffff"/>
          <stop offset="1" stop-color="#c9ccd0"/>
        </linearGradient>
        <linearGradient id="photo-pipes" x1="0" y1="0" x2="1" y2="1">
          <stop offset="0" stop-color="#dfe3e7"/>
          <stop offset=".55" stop-color="#9aa2ab"/>
          <stop offset="1" stop-color="#5a6470"/>
        </linearGradient>
        <linearGradient id="photo-plumber" x1="0" y1="0" x2="1" y2="1">
          <stop offset="0" stop-color="#e8eaee"/>
          <stop offset=".5" stop-color="#4a78b8"/>
          <stop offset="1" stop-color="#9a5a4c"/>
        </linearGradient>
      </defs>

      <rect class="footer-panel" x="0" y="620" width="600" height="230" fill="#e4e6e9"/>
      <path d="M0 190 C150 140 330 100 600 100 L600 132 C330 132 160 170 0 220 Z" fill="#8e9399"/>
      <path d="M0 215 C160 165 330 135 600 135 L600 620 C420 640 200 660 0 690 Z" fill="url(#blue-field)"/>
      <path d="M0 585 L420 565 Q450 563 450 592 L450 660 Q450 686 420 688 L0 705 Z" fill="#1c1c1e"/>
      <rect x="298" y="295" width="292" height="100" rx="22" fill="url(#grey-box)"/>

      <circle cx="125" cy="240" r="116" fill="#ffffff"/>
      <circle cx="125" cy="240" r="108" fill="#1e7fd6"/>
      <circle cx="125" cy="240" r="100" fill="url(#photo-pipes)" role="img" aria-label="Photo of a plumber tightening a chrome sink trap with a wrench"/>

      <circle cx="478" cy="520" r="104" fill="#ffffff"/>
      <circle cx="478" cy="520" r="97" fill="#1e7fd6"/>
      <circle cx="478" cy="520" r="90" fill="url(#photo-plumber)" role="img" aria-label="Photo of a smiling plumber kneeling beside pipes and wrenches"/>

      <polygon transform="translate(225 350) scale(1.15)" fill="#ffffff" stroke="#c9ccd0" stroke-width="1.8"
        points="62,0 50.2,13.5 53.7,31 36.8,36.8 31,53.7 13.5,50.2 0,62 -13.5,50.2 -31,53.7 -36.8,36.8 -53.7,31 -50.2,13.5 -62,0 -50.2,-13.5 -53.7,-31 -36.8,-36.8 -31,-53.7 -13.5,-50.2 0,-62 13.5,-50.2 31,-53.7 36.8,-36.8 53.7,-31 50.2,-13.5"/>
    </svg>

    <div class="brand-name">LOGO</div>
    <div class="services">
      <div class="line-1">Plumbing, draining</div>
      <div class="line-2">AND GASFITTING</div>
    </div>

    <h1 class="headline">Quality work at<br>a decent price</h1>
    <p class="tagline">Local plumber</p>
    <p class="gst-note">No GST payable,<br>saving you additional<br><strong>10% on your bill</strong></p>

    <div class="discount">
      <div class="amount">15% OFF</div>
      <div class="detail">Your overall bill</div>
    </div>

    <div class="offer">
      <div class="main">A free hot water<br>health check</div>
      <div class="sub">and replacement quote</div>
    </div>

    <div class="call-to-action">
      <div class="lead">To make an appointment</div>
      <div class="name">Call or email Marty</div>
      <div class="alt">or alternatively make a booking directly on the website</div>
    </div>

    <ul class="contact-list">
      <li><svg viewBox="0 0 16 16"><path d="M3 1 L6 1 L7 5 L5 6.5 C6 9 7 10 9.5 11 L11 9 L15 10 L15 13 C15 14.5 14 15 13 15 C6.5 15 1 9.5 1 3 C1 2 1.5 1 3 1 Z"/></svg>0400 555 218</li>
      <li><svg viewBox="0 0 16 16"><path d="M1 3 H15 V13 H1 Z M1.8 3.8 L8 8.8 L14.2 3.8 Z" fill-rule="evenodd"/></svg>marty@brookwaterplumbing.com</li>
      <li><svg viewBox="0 0 16 16"><circle cx="8" cy="8" r="7"/></svg>www.brookwaterplumbing.com</li>
    </ul>

    <p class="fine-print">
      Offer valid between 15 August 2016 to 15 October 2016<br>
      ^Valid until 30 September 2016<br>
      Quote valid for 12 months from the quote date
    </p>
  </article>
</body>
</html>
```